Investment Memorandum Document

IM for Harbourline Lending Fund - is the document that needs work

Make sure it is all done in MS WORD so that i or lawyers can edit some words if required

the IM is NOT final but its 95% of the way there. Maybe a few more pages and wording changes - but that is something i can do i guess or you can easier adjust

Just to typeset and pretty it all up - a few sample finished products have been uploaded for reference.

KPT IM is the one i like - but feel free to show off your skills

put 1.2 to 1.8 all in contrasting row tables

Target Market(s)

Individual and Institutional investors with money

Industry/Entity Type

Investment Banking

Colors

Designer to choose colors to be used in the design.

Requirements
Must have
• clear professional layout and easy on the eye
• https://www.filebarn-example.net/sh/84m7t55xqk2wbnr/QQzdLeMu8RplbqTYAXNW47Ko?dl=0
• use the link above for high res images
Nice to have
• pictures and graphics
Should not have
• cartoons

```html
<!DOCTYPE html>
<html lang="en">
<head>
<meta charset="utf-8">
<title>Harbourline Diversified Commercial Income Fund – Information Memorandum Spreads</title>
<link rel="stylesheet" href="https://fonts.googleapis.com/css2?family=Montserrat:wght@300;400;600&family=Open+Sans:wght@400;600&display=swap">
<style>
:root{
  --backdrop:#a9abae;
  --paper:#ffffff;
  --gold:#c4904a;
  --gold-dark:#9c6a2c;
  --gold-light:#e6c48d;
  --ink:#4a4a4a;
  --ink-soft:#8a8a8a;
  --rule:#d9d2c7;
  --night:#14233a;
  --night-mid:#2c4a6e;
  --box-grey:#7d7f82;
}
*{box-sizing:border-box;margin:0;padding:0}
html,body{width:1200px;height:650px;overflow:hidden}
body{background:linear-gradient(135deg,#b4b6b9,var(--backdrop) 60%,#9fa1a4);font-family:"Open Sans",Arial,sans-serif;color:var(--ink);position:relative}
.page{position:absolute;width:212px;height:274px;background:var(--paper);box-shadow:0 2px 6px rgba(0,0,0,.25);overflow:hidden}
.row-top{top:42px}.row-bottom{top:326px}
.col-1{left:50px}.col-2{left:270px}.col-3{left:490px}.col-4{left:710px}.col-5{left:930px}
.page-body{position:absolute;left:14px;right:14px;top:16px}
.page-title{font-family:"Montserrat",Arial,sans-serif;font-weight:300;color:var(--gold);font-size:8px;letter-spacing:.2px;margin-bottom:8px}
.sub-head{font-family:"Montserrat",Arial,sans-serif;font-weight:600;color:var(--gold);font-size:3.2px;text-transform:uppercase;margin:4px 0 2px}
.section-head{font-family:"Montserrat",Arial,sans-serif;color:var(--gold);font-size:4.4px;margin:4px 0 2px}
p,li{font-size:2.6px;line-height:1.45;margin-bottom:2.6px;text-align:justify}
ul{padding-left:5px}
.page-footer{position:absolute;left:14px;bottom:6px;font-size:2.2px;color:var(--ink-soft)}
.corner{position:absolute;right:0;bottom:0}
/* cover */
.brand{position:absolute;top:26px;right:22px;display:flex;align-items:center;gap:3px}
.brand-mark{width:8px;height:8px;background:var(--gold)}
.brand-name{font-family:"Montserrat",Arial,sans-serif;font-weight:400;font-size:8px;letter-spacing:1.5px;color:var(--ink)}
.brand-tag{position:absolute;top:36px;right:22px;font-size:2.4px;letter-spacing:1.2px;color:var(--ink)}
.cover-title{position:absolute;top:62px;right:22px;text-align:right;font-family:"Montserrat",Arial,sans-serif;font-weight:300;color:var(--gold);font-size:7.4px;line-height:1.25}
.cover-sub{position:absolute;top:94px;right:22px;font-family:"Montserrat",Arial,sans-serif;font-weight:300;font-size:6px;color:var(--ink)}
.photo{position:absolute;left:0;right:0;bottom:0;background:linear-gradient(160deg,var(--night-mid),var(--night) 55%,#0b1524);}
.cover-photo{top:110px}
.cover-credits{position:absolute;left:16px;bottom:22px;color:#fff;font-size:2.4px;line-height:1.5}
.cover-credits strong{font-weight:600}
/* toc */
.toc-list{list-style:none;padding:0}
.toc-list li{display:flex;justify-content:space-between;font-size:3.4px;text-transform:uppercase;color:var(--ink);margin-bottom:3.2px;text-align:left}
.toc-body{left:32px;right:52px;top:18px}
.toc-photo{top:150px}
/* tables */
.feature-table{width:100%;border-collapse:collapse}
.feature-table td{font-size:2.5px;line-height:1.45;vertical-align:top;padding:2.5px 0;border-top:.4px solid var(--rule)}
.feature-table td.label{color:var(--gold);width:30%;padding-right:4px;font-size:2.6px}
/* diagram */
.fund-diagram{display:block;margin:3px auto}
.sign-off p{margin-bottom:1px;text-align:left}
</style>
</head>
<body>

<!-- Cover -->
<section class="page row-top col-1 cover">
  <div class="brand"><span class="brand-mark"></span><span class="brand-name">HARBOURLINE</span></div>
  <div class="brand-tag">ASSET MANAGEMENT</div>
  <h1 class="cover-title">Diversified Commercial<br>Income Fund</h1>
  <div class="cover-sub">Information Memorandum</div>
  <div class="photo cover-photo" role="img" aria-label="Night city skyline with illuminated towers and light trails"></div>
  <svg class="corner" width="212" height="164" viewBox="0 0 212 164" style="bottom:0">
    <defs><linearGradient id="goldCover" x1="0" y1="0" x2="1" y2="1"><stop offset="0" stop-color="#e6c48d"/><stop offset="1" stop-color="#9c6a2c"/></linearGradient></defs>
    <polygon points="0,0 212,0 212,10 0,40" fill="#fff"/>
    <polygon points="0,0 0,40 90,26" fill="#fff" opacity=".6"/>
    <polygon points="212,52 212,164 120,164" fill="url(#goldCover)" opacity=".95"/>
    <polygon points="0,60 0,164 40,164" fill="url(#goldCover)" opacity=".55"/>
  </svg>
  <div class="cover-credits"><strong>Investment Manager</strong><br>Harbourline Asset Management Pty Ltd<br><br><strong>Trustee</strong><br>Keelpoint Trust Corporation Pty Ltd</div>
</section>

<!-- Table of content -->
<section class="page row-top col-2">
  <div class="page-body toc-body">
    <h2 class="page-title">Table of Content</h2>
    <ul class="toc-list">
      <li><span>Message from the Managing Director</span><span>5</span></li>
      <li><span>The Fund</span><span>6</span></li>
      <li><span>The Loans</span><span>12</span></li>
      <li><span>Risks</span><span>17</span></li>
      <li><span>Fees and Costs</span><span>20</span></li>
      <li><span>Management of the Fund</span><span>22</span></li>
      <li><span>Taxation Information</span><span>26</span></li>
      <li><span>Additional Information</span><span>31</span></li>
      <li><span>Application Process</span><span>34</span></li>
      <li><span>Glossary</span><span>36</span></li>
      <li><span>Corporate Directory</span><span>38</span></li>
    </ul>
  </div>
  <div class="photo toc-photo" role="img" aria-label="Upward view of glass office towers at night"></div>
  <svg class="corner" width="212" height="124" viewBox="0 0 212 124">
    <defs><linearGradient id="goldToc" x1="0" y1="0" x2="1" y2="1"><stop offset="0" stop-color="#e6c48d"/><stop offset="1" stop-color="#9c6a2c"/></linearGradient></defs>
    <polygon points="0,0 212,0 0,60" fill="#fff"/>
    <polygon points="212,40 212,124 140,124" fill="url(#goldToc)"/>
  </svg>
</section>

<!-- Important notice 1 -->
<section class="page row-top col-3">
  <div class="page-body">
    <h2 class="page-title">IMPORTANT NOTICE</h2>
    <p>This information memorandum is dated 2024 and is issued by Keelpoint Trust Corporation Pty Ltd as the trustee of the Harbourline Diversified Commercial Income Fund.</p>
    <p>The purpose of this IM is to provide information for prospective investors to decide whether they wish to invest in the Fund.</p>
    <p>The Trustee has appointed Harbourline Asset Management Pty Ltd as the investment manager of the Fund under the Investment Management Agreement.</p>
    <p>The purpose of this IM is to provide information for prospective investors to decide whether they wish to invest in the Fund. Units are offered in different classes, each with its own terms.</p>
    <p>The offer made under this IM is only available to persons who qualify as wholesale clients under the Corporations Act.</p>
    <h3 class="sub-head">No disclosure required</h3>
    <p>This IM is intended to provide potential investors with information only and does not constitute a product disclosure statement or other disclosure document required by the Corporations Act.</p>
    <h3 class="sub-head">Restrictions on distribution</h3>
    <p>This IM does not constitute, and may not be used for the purposes of, an offer of Units or an invitation to apply for Units in any jurisdiction in which such an offer would be unlawful.</p>
    <p>No action has been taken to register or qualify interests in the Fund in any jurisdiction outside Australia. Persons who receive this IM must inform themselves about and observe any restrictions.</p>
    <p>In particular, this product has not been and will not be registered under the US Securities Act and may not be offered or sold in the United States.</p>
  </div>
  <div class="page-footer">Page 02 &nbsp; Harbourline Diversified Commercial Income Fund · Information Memorandum</div>
</section>

<!-- Important notice 2 -->
<section class="page row-top col-4">
  <div class="page-body">
    <h2 class="page-title">IMPORTANT NOTICE</h2>
    <p>With respect to Australian jurisdiction, this IM has been prepared on the basis that the prospective investors are wholesale clients or sophisticated investors.</p>
    <p>Accordingly, this IM is not a product disclosure statement and does not contain all of the information required in one.</p>
    <p>The Trustee may in the future take actions to offer interests in the Fund in other jurisdictions.</p>
    <h3 class="sub-head">No responsibility for contents of document</h3>
    <p>To the maximum extent permitted by law, none of the Trustee, the Investment Manager or any of their associates makes any representation as to the accuracy or completeness of this IM.</p>
    <p>This IM does not purport to contain all the information that a prospective investor may require in evaluating the Fund.</p>
    <p>This IM must be read in conjunction with the Trust Deed, which is available free of charge on request from the Trustee.</p>
    <h3 class="sub-head">No distribution</h3>
    <p>Distribution of this IM to any person other than the person receiving a copy is unauthorised. Any photocopying or disclosure of its contents is prohibited.</p>
    <h3 class="sub-head">Not regulated by APRA</h3>
    <p>The Trustee is not authorised under the Banking Act and is not supervised by APRA. Investments in the Fund are not covered by deposit protection.</p>
    <h3 class="sub-head">Forward-looking statements</h3>
    <p>This IM includes forward-looking statements that may contain words such as believe, intend, estimate and expect. Such statements involve known and unknown risks and uncertainties which may cause actual results to differ.</p>
  </div>
  <div class="page-footer">Page 03 &nbsp; Harbourline Diversified Commercial Income Fund · Information Memorandum</div>
</section>

<!-- Important notice 3 -->
<section class="page row-top col-5">
  <div class="page-body">
    <h2 class="page-title">IMPORTANT NOTICE</h2>
    <p>Any forward-looking statements are based on numerous assumptions regarding the present and future business, investment strategies and markets in which the Fund will operate.</p>
    <h3 class="sub-head">Independent advice recommended</h3>
    <p>Prospective investors should not construe the contents of this IM as tax, legal or investment advice. The information contained in this IM is general information only and does not take into account your objectives, financial situation or needs. Investors should seek appropriate professional advice before deciding to invest.</p>
    <h3 class="sub-head">No guarantee</h3>
    <p>An investment in the Fund is subject to investment risk, including loss of income and capital invested. No party guarantees the performance of the Fund or any particular rate of return.</p>
    <h3 class="sub-head">Trustee limitation of liability</h3>
    <p>Except in certain circumstances, the Trustee enters into transactions for the Fund in its capacity as trustee only and its liability is limited to the assets of the Fund.</p>
    <h3 class="sub-head">Updated information</h3>
    <p>The information contained in this IM may change and the IM may be updated or replaced from time to time. Updated information can be obtained by contacting the Trustee.</p>
    <h3 class="sub-head">Confidentiality</h3>
    <p>This IM is confidential and is provided to prospective investors for them to consider investing in the Fund.</p>
    <h3 class="sub-head">Glossary</h3>
    <p>Certain capitalised words and expressions used in this IM are defined in the Glossary. All amounts are in Australian dollars.</p>
  </div>
  <div class="page-footer">Page 04 &nbsp; Harbourline Diversified Commercial Income Fund · Information Memorandum</div>
</section>

<!-- Message from the managing director -->
<section class="page row-bottom col-1">
  <div class="page-body">
    <h2 class="page-title">Message from the Managing Director</h2>
    <p>Dear investor,</p>
    <p>On behalf of Harbourline Asset Management, it is my pleasure to invite you to participate in our flagship Diversified Commercial Income Fund.</p>
    <p>Harbourline is supported by a dedicated and experienced team of investment and property professionals providing credit solutions to exclusive opportunities.</p>
    <p>At the core of our business are the same disciplines, due diligence and values which you afford to your own money.</p>
    <p>We are proud to partner with Northgate Property Group as our flagship fund developer, a group with a strong record in commercial projects.</p>
    <p>The Fund is a managed investment scheme established as a unit trust. Investment is limited to wholesale clients.</p>
    <p>The Fund will initially raise capital to provide investors with regular fixed monthly returns.</p>
    <p>The key benefits of investing in the Fund include:</p>
    <ul>
      <li>attractive fixed income distributions;</li>
      <li>exposure to a significant high-end commercial development lending portfolio;</li>
      <li>investment in a Fund with a Trustee that is independent from the Manager;</li>
      <li>all fees being absorbed by the Investment Manager.</li>
    </ul>
    <p>As with any investment, there are risks associated with an investment in the Fund and I encourage you to read this IM thoroughly.</p>
    <div class="sign-off"><p>Yours faithfully,</p><p>Daniel Ashcroft</p><p>Managing Director</p></div>
  </div>
  <svg class="corner" width="90" height="70" viewBox="0 0 90 70"><defs><linearGradient id="g1" x1="0" y1="0" x2="1" y2="1"><stop offset="0" stop-color="#e6c48d"/><stop offset="1" stop-color="#9c6a2c"/></linearGradient></defs><polygon points="90,0 90,70 10,70" fill="url(#g1)"/></svg>
  <div class="page-footer">Page 05 &nbsp; Harbourline Diversified Commercial Income Fund · Information Memorandum</div>
</section>

<!-- The Fund -->
<section class="page row-bottom col-2">
  <div class="page-body">
    <h2 class="page-title">1. &nbsp;The Fund</h2>
    <h3 class="section-head">1.1 &nbsp;Fund Outline</h3>
    <p>The Fund is an unregistered managed investment scheme which pools investors' monies and invests in loans predominantly used for property investment and development projects. The Fund was established by a Trust Deed.</p>
    <svg class="fund-diagram" width="170" height="64" viewBox="0 0 170 64">
      <g fill="none" stroke="#9a9a9a" stroke-width=".5">
        <line x1="85" y1="10" x2="85" y2="22"/><line x1="48" y1="30" x2="68" y2="30"/><line x1="102" y1="30" x2="122" y2="30"/>
        <line x1="85" y1="38" x2="85" y2="46"/><line x1="30" y1="46" x2="145" y2="46"/>
        <line x1="30" y1="46" x2="30" y2="52"/><line x1="85" y1="46" x2="85" y2="52"/><line x1="145" y1="46" x2="145" y2="52"/>
      </g>
      <rect x="72" y="2" width="26" height="8" fill="#7d7f82"/>
      <rect x="12" y="22" width="36" height="14" fill="#7d7f82"/>
      <rect x="68" y="22" width="34" height="16" fill="#c4904a"/>
      <rect x="122" y="22" width="40" height="14" fill="#7d7f82"/>
      <rect x="12" y="52" width="36" height="8" fill="#dce4f0"/>
      <rect x="67" y="52" width="36" height="8" fill="#dce4f0"/>
      <rect x="127" y="52" width="36" height="8" fill="#dce4f0"/>
      <g font-family="Open Sans, Arial, sans-serif" font-size="2.6" text-anchor="middle" fill="#fff">
        <text x="85" y="7">Investors</text>
        <text x="30" y="30">Investment Manager</text>
        <text x="85" y="31">Harbourline Fund</text>
        <text x="142" y="30">Administrator</text>
      </g>
      <g font-family="Open Sans, Arial, sans-serif" font-size="2.6" text-anchor="middle" fill="#4a4a4a">
        <text x="30" y="57">Cash Units</text><text x="85" y="57">Class 1 Loan Units</text><text x="145" y="57">Class 2 Loan Units</text>
      </g>
    </svg>
    <p>The Fund will invest predominantly in loans used in connection with development projects managed or developed by Northgate Property Group.</p>
    <p>All investments are made in accordance with the Fund's Lending Guidelines.</p>
    <ul>
      <li>A class of Cash Units in the Fund that are referable to a Bank Deposit Product.</li>
      <li>A class of Loan Units in the Fund that are referable to a portfolio of loans secured by registered mortgages.</li>
    </ul>
    <p>Key benefits of investing in the Fund:</p>
    <ul>
      <li>The Fund has an independent trustee providing oversight.</li>
      <li>Underlying projects are undertaken by an experienced group.</li>
      <li>Transparency through regular investment reports.</li>
      <li>Audited by an independent firm.</li>
    </ul>
  </div>
  <svg class="corner" width="70" height="60" viewBox="0 0 70 60"><defs><linearGradient id="g2" x1="0" y1="0" x2="1" y2="1"><stop offset="0" stop-color="#e6c48d"/><stop offset="1" stop-color="#9c6a2c"/></linearGradient></defs><polygon points="70,0 70,60 0,60" fill="url(#g2)"/></svg>
  <div class="page-footer">Page 06 &nbsp; Harbourline Diversified Commercial Income Fund · Information Memorandum</div>
</section>

<!-- Key features -->
<section class="page row-bottom col-3">
  <div class="page-body">
    <h3 class="section-head">1.2 &nbsp;Key Features</h3>
    <p>The table below is only a summary of the key features of an investment in the Fund. It is not intended to be exhaustive.</p>
    <table class="feature-table">
      <tr><td class="label">Trustee</td><td>Keelpoint Trust Corporation Pty Ltd is the trustee of the Fund and will be responsible for holding title to the Fund's assets.</td></tr>
      <tr><td class="label">Investment Manager</td><td>Harbourline Asset Management Pty Ltd has been appointed as the investment manager of the Fund and is responsible for managing the Fund's assets and the day-to-day operations.</td></tr>
      <tr><td class="label">Administration Manager</td><td>An independent administrator has been appointed and is responsible for unit registry, accounting and fund reporting.</td></tr>
      <tr><td class="label">Investment objective</td><td>The Investment Manager's aim is to provide investors with attractive fixed income returns derived through investment in a portfolio of commercial loans made to special purpose vehicles. Typically, Northgate Property Group will be the controlling shareholder of each vehicle and will control the development project.<br><br>Northgate Property Group is a related entity of the Investment Manager.</td></tr>
      <tr><td class="label">Who can invest in the Fund?</td><td>Investment in the Fund is only available to parties who are at least 18 years of age. If residing in Australia, investors must invest at least $500,000 or provide a certificate from a qualified accountant, or be a professional investor.<br><br>For non-Australian residents, please contact the Trustee for information on qualifying criteria.</td></tr>
    </table>
  </div>
  <div class="page-footer">Page 10 &nbsp; Harbourline Diversified Commercial Income Fund · Information Memorandum</div>
</section>

<!-- Target return and fund units -->
<section class="page row-bottom col-4">
  <div class="page-body">
    <table class="feature-table">
      <tr><td class="label">Target Returns</td><td><strong>Cash Units</strong><br>The target return for Cash Units, before tax, after all fees, is the cash rate plus 1.5% p.a.<br><br><strong>Loan Units</strong><br>The target return of each class of Loan Units is: Class 1 Loan Units 8% per annum after fees; Class 2 Loan Units 10% per annum after fees.<br><br>The Target Return is not guaranteed. The Fund may not be successful in meeting this objective.</td></tr>
      <tr><td class="label">Minimum Initial Investment Amount</td><td><strong>Cash Units</strong><br>The minimum initial investment for Cash Units is $100,000 from a Qualifying Investor.<br><br><strong>Loan Units</strong><br>The minimum initial investment for Loan Units is $100,000 from a Qualifying Investor.<br><br>However, the Trustee may accept lower amounts at its absolute discretion.</td></tr>
    </table>
    <h3 class="section-head">1.3 &nbsp;Fund Units</h3>
    <p class="sub-head">Class of Units</p>
    <p>The Fund comprises of multiple classes of Units which includes Cash Units and Loan Units. The following classes of Units are issued pursuant to this IM.</p>
    <p><strong>Cash Units</strong><br>Cash Units comprise a portfolio of bank deposit products only.</p>
    <p><strong>Class 1 and Class 2 Loan Units</strong><br>Loan Units comprise a portfolio of loan investments which include senior and mezzanine debt.</p>
    <p class="sub-head">Issue of Units</p>
    <p>Cash Units will be issued monthly within 5 Business Days after the end of the month in which the application is received and accepted.</p>
    <p>Loan Units will be issued monthly within 5 Business Days after the end of the month in which the application is accepted.</p>
  </div>
  <svg class="corner" width="60" height="50" viewBox="0 0 60 50"><defs><linearGradient id="g4" x1="0" y1="0" x2="1" y2="1"><stop offset="0" stop-color="#e6c48d"/><stop offset="1" stop-color="#9c6a2c"/></linearGradient></defs><polygon points="60,0 60,50 0,50" fill="url(#g4)"/></svg>
  <div class="page-footer">Page 11 &nbsp; Harbourline Diversified Commercial Income Fund · Information Memorandum</div>
</section>

<!-- Distributions -->
<section class="page row-bottom col-5">
  <div class="page-body">
    <p class="sub-head">Unit Price</p>
    <p>It is intended that Units will be issued at $1.00, however the Unit price is based on the underlying value of the Fund's assets referable to the particular class of Units.</p>
    <p>The withdrawal price for a Unit is also based on the underlying value of the Fund's assets.</p>
    <h3 class="section-head">1.4 &nbsp;Distributions</h3>
    <p>The rate and frequency of distributions will depend upon the class of Units held by the investor.</p>
    <p><strong>Cash Units</strong><br>It is intended that distributions on Cash Units will be calculated and paid quarterly within 5 Business Days of the end of each calendar quarter.</p>
    <p>Investors will receive a proportion of the income referable to Cash Units based on the number of Cash Units they hold in relation to the total number of Cash Units on issue.</p>
    <p><strong>Loan Units</strong><br>It is intended that distributions on Loan Units will be calculated and paid half-yearly in arrears within 20 Business Days following the end of each financial year.</p>
    <p>Investors will receive a proportion of the income referable to Loan Units based on the number of Loan Units they hold.</p>
    <p>Distributions may be paid and reinvested in Loan Units if the investor makes an election in the Application Form.</p>
    <h3 class="section-head">1.5 &nbsp;Withdrawal rights</h3>
    <p>An investor's ability to withdraw from the Fund will depend upon the class of Units held by the investor.</p>
    <p>The withdrawal price for a Unit is also based on the underlying value of the assets referable to the particular class of Units.</p>
    <p><strong>Cash Units</strong><br>Generally, Cash Units may be withdrawn at any time by lodging a Withdrawal Request with the Trustee at least 1 Business Day prior to the end of a calendar month.</p>
  </div>
  <svg class="corner" width="80" height="60" viewBox="0 0 80 60"><defs><linearGradient id="g5" x1="0" y1="0" x2="1" y2="1"><stop offset="0" stop-color="#e6c48d"/><stop offset="1" stop-color="#9c6a2c"/></linearGradient></defs><polygon points="80,0 80,60 0,60" fill="url(#g5)"/></svg>
  <div class="page-footer">Page 12 &nbsp; Harbourline Diversified Commercial Income Fund · Information Memorandum</div>
</section>

</body>
</html>
```